Korvane Plumbing Business cards

Company is Korvane Plumbing.
name Dorian Malvessey, I am a plumber, drainer, gasfitter and roofer
Mobile: 0461 590 314
Email address: info@korvaneplumbing.example (check out my website for some ideas)
Website: www.korvaneplumbing.example
ABN: 42 198 603 771
LIC: 516042D

I am reliable all round plumber. I am a 24 hour emergency service. Korvane Plumbing is a professional plumbing service in the Illawarra, South Coast, Southern Sydney and Southern Highland regions of NSW. We offer a 24 hour emergency service for piece of mind to our customers. Call us now to see how we can help you. Korvane Plumbing approaches every job with attention to detail and excellent customer service. With our superior workmanship you can be confident that the job will be done right the first time around. You can rest assured with results that are guaranteed to last.

Target Market(s)

the general public

Contact Information for Business Card

look up website for some ideas something with similar colours to logo and new modern and to catch the eye.

Colors
fdfdfd
ffffff
000000
7f7f7f
aaaaaa
33a6d7
0492cd

Requirements
Must have
• all contact details
• company- Korvane Plumbing
• name- Dorian Malvessey
• number mobile- 0461 590 314
• Email address- info@korvaneplumbing.example
• Website- www.korvaneplumbing.example
• ABN- 42 198 603 771
• LIC- 516042D

```html
<!DOCTYPE html>
<html lang="en">
<head>
<meta charset="utf-8">
<title>Korvane Plumbing – Business Card</title>
<link rel="stylesheet" href="https://fonts.googleapis.com/css2?family=Arimo:wght@400;700&display=swap">
<style>
  :root {
    --paper: #ffffff;
    --backdrop: #e9e9e9;
    --ink: #000000;
    --grey: #7f7f7f;
    --rule: #aaaaaa;
    --divider: #d6d6d6;
    --blue: #33a6d7;
    --blue-deep: #0492cd;
    --back-blue: #1b9bd0;
  }
  * { box-sizing: border-box; margin: 0; padding: 0; }
  html, body {
    width: 1200px; height: 900px; overflow: hidden;
    background: var(--backdrop);
    font-family: "Arimo", Arial, sans-serif;
  }
  .card {
    position: absolute; left: 270px;
    width: 660px; height: 378px;
    box-shadow: 0 6px 22px rgba(0,0,0,0.14);
    overflow: hidden;
  }

  /* back side */
  .card-back { top: 48px; background: var(--back-blue); }
  .back-brand {
    position: absolute; inset: 0;
    display: flex; flex-direction: column; align-items: center; justify-content: center; gap: 16px;
  }
  .back-ring {
    width: 58px; height: 58px; border-radius: 50%;
    border: 6px solid var(--paper);
  }
  .back-name {
    color: var(--paper); font-weight: 700; font-size: 34px; line-height: 1;
  }

  /* front side */
  .card-front { top: 474px; background: var(--paper); }
  .brand {
    position: absolute; left: 136px; top: 120px;
    width: 160px; height: 130px;
    display: flex; flex-direction: column; align-items: center; justify-content: center; gap: 10px;
  }
  .brand-dot {
    width: 30px; height: 30px; border-radius: 50%;
    background: var(--blue);
  }
  .brand-name {
    color: var(--blue);
    font-weight: 700; font-size: 21px; line-height: 1.1;
    text-align: center;
  }
  .divider {
    position: absolute; left: 320px; top: 111px;
    width: 1px; height: 141px; background: var(--divider);
  }
  .details { position: absolute; left: 344px; top: 102px; }
  .person {
    color: var(--blue-deep); font-weight: 700; font-size: 20px; line-height: 24px;
    margin-bottom: 9px;
  }
  .reg { font-size: 14px; color: var(--ink); line-height: 16px; }
  .reg b { color: var(--blue-deep); }
  .contacts { list-style: none; margin-top: 13px; }
  .contacts li {
    display: flex; align-items: center; gap: 9px;
    font-size: 14px; color: var(--ink); height: 20px;
  }
  .contacts svg { width: 16px; height: 16px; flex: none; }
  .band {
    position: absolute; left: 0; top: 321px;
    width: 100%; height: 34px;
    background: var(--blue-deep);
  }
  .band-end {
    position: absolute; right: 0; top: 0;
    width: 56px; height: 100%;
    background: var(--grey);
  }
  .band-seal {
    position: absolute; left: 554px; top: -5px;
    width: 44px; height: 44px; border-radius: 50%;
    background: var(--paper); border: 2px solid var(--rule);
  }
</style>
</head>
<body>
  <div class="card card-back">
    <div class="back-brand">
      <span class="back-ring"></span>
      <span class="back-name">Korvane Plumbing</span>
    </div>
  </div>

  <div class="card card-front">
    <div class="brand">
      <span class="brand-dot"></span>
      <span class="brand-name">Korvane<br>Plumbing</span>
    </div>
    <div class="divider"></div>
    <div class="details">
      <p class="person">Dorian Malvessey</p>
      <p class="reg"><b>ABN:</b> 42 198 603 771</p>
      <p class="reg"><b>LIC:</b> 516042D</p>
      <ul class="contacts">
        <li>
          <svg viewBox="0 0 24 24" aria-hidden="true"><rect x="6" y="2" width="12" height="20" rx="2.5" fill="none" stroke="#0492cd" stroke-width="2"/><line x1="10" y1="18.5" x2="14" y2="18.5" stroke="#0492cd" stroke-width="1.6"/></svg>
          0461 590 314
        </li>
        <li>
          <svg viewBox="0 0 24 24" aria-hidden="true"><rect x="2" y="5" width="20" height="14" fill="#0492cd"/><polyline points="2,5 12,13 22,5" fill="none" stroke="#ffffff" stroke-width="1.6"/></svg>
          info@korvaneplumbing.example
        </li>
        <li>
          <svg viewBox="0 0 24 24" aria-hidden="true"><circle cx="12" cy="12" r="10" fill="#0492cd"/><g fill="none" stroke="#ffffff" stroke-width="1.3"><ellipse cx="12" cy="12" rx="4.5" ry="10"/><line x1="2" y1="12" x2="22" y2="12"/><line x1="12" y1="2" x2="12" y2="22"/><path d="M4 7h16M4 17h16"/></g></svg>
          www.korvaneplumbing.example
        </li>
      </ul>
    </div>
    <div class="band">
      <div class="band-end"></div>
      <div class="band-seal"></div>
    </div>
  </div>
</body>
</html>
```